QRN Frame table flyer for Stratum Machinery

Design a flyer that will be used on social media to promote our QRN Portal table. This is to promote our tables to new market and under a new brand name. Design should we print the flyer to be on a 11x8.5 paper.
Included is the two accepted logo configuration of our brand - Stratum Machinery along with 2 photos of our latest installation. If you can change the logo on the installation from LUP Holdings to Stratum Machinery please.
Highlights of our machine to be included on flyer:
- Available in 12’ or 14’ wide
- Side or end eject
Highlights of our machine to add to flyer if your design can incorporate it:
- Heavy duty table top.
- T-slot opening for jigging
- All tables built to customers length requirements

For contact information to be put on flyer, Dario at (800)555-0182 or dario@lupholdings-example.ca
Will have the website address added here as soon as it is done.

Please incorporate the following line (will prefer to have this at the bottom) : Stratum Machinery a brand manufactured by LUP Holdings Inc.

Our equipment colors are Clam white and Orange like seen on the equipment pictures.

Target Market(s)

Truss Manufacturers

Industry/Entity Type

Pre fabricated housing market and component manufacturers

Font styles to use
Sans Serif

Colors
EE7325
F08F49
F5BC92
FAE3D3
FDF4ED

Requirements
Must have
• a few highlights that are in the description
Nice to have
• Added to project description

```html
<!DOCTYPE html>
<html lang="en">
<head>
<meta charset="utf-8">
<title>QRN Portal Table Flyer – Stratum Machinery</title>
<link rel="stylesheet" href="https://fonts.googleapis.com/css2?family=Open+Sans:wght@600;700;800&family=Oswald:wght@500;600&display=swap">
<style>
  :root {
    --orange: #EE7325;
    --orange-light: #F08F49;
    --peach: #F5BC92;
    --cream: #FAE3D3;
    --clam: #FDF4ED;
    --ink: #111111;
    --steel: #4a4a4c;
    --backdrop: #e4e0e4;
  }
  * { box-sizing: border-box; margin: 0; padding: 0; }
  html, body { width: 1200px; height: 800px; overflow: hidden; background: var(--backdrop); }
  .flyer {
    position: absolute; left: 314px; top: 30px;
    width: 572px; height: 740px; overflow: hidden;
    background: var(--clam);
    font-family: "Open Sans", sans-serif;
    box-shadow: 0 6px 18px rgba(0,0,0,.18);
  }
  .flyer__art { position: absolute; inset: 0; }
  .brand {
    position: absolute; right: 26px; top: 36px; width: 220px;
    display: flex; align-items: center; gap: 10px;
    color: var(--cream); font-weight: 800; font-size: 19px; letter-spacing: 1px;
    text-transform: uppercase; line-height: 1.1;
  }
  .brand__mark { width: 16px; height: 16px; background: var(--cream); flex: none; }
  .highlights { position: absolute; left: 34px; top: 196px; width: 300px; }
  .highlights__title {
    color: var(--orange); font-weight: 800; font-size: 19px;
    text-transform: uppercase; margin-bottom: 8px;
  }
  .highlights__list { list-style: none; }
  .highlights__item {
    display: flex; align-items: flex-start; gap: 8px;
    color: var(--ink); font-weight: 700; font-size: 14px; line-height: 1.25; margin-bottom: 5px;
  }
  .tick { width: 13px; height: 13px; flex: none; margin-top: 2px; }
  .contact {
    position: absolute; left: 0; bottom: 0; width: 100%; height: 104px;
    background: var(--orange); color: var(--clam);
  }
  .contact__tab {
    position: absolute; left: 170px; top: -20px; padding: 4px 20px;
    background: var(--ink); color: var(--orange);
    font-family: "Oswald", sans-serif; font-weight: 600; font-size: 24px;
    text-transform: uppercase; letter-spacing: .5px;
  }
  .contact__name {
    position: absolute; left: 26px; top: 22px;
    font-weight: 800; font-size: 17px; text-transform: uppercase;
  }
  .contact__list {
    position: absolute; left: 26px; top: 52px; right: 20px;
    list-style: none; display: flex; flex-wrap: wrap; gap: 6px 22px;
    font-weight: 600; font-size: 13px;
  }
  .contact__item { display: flex; align-items: center; gap: 6px; }
  .icon { width: 14px; height: 14px; flex: none; }
</style>
</head>
<body>
<article class="flyer">
  <svg class="flyer__art" viewBox="0 0 572 740" width="572" height="740">
    <defs>
      <linearGradient id="plantTones" x1="0" y1="0" x2="1" y2="1">
        <stop offset="0" stop-color="#8d8a86"/>
        <stop offset=".45" stop-color="#c9c4bb"/>
        <stop offset="1" stop-color="#9a7a52"/>
      </linearGradient>
      <linearGradient id="floorTones" x1="0" y1="0" x2="1" y2="1">
        <stop offset="0" stop-color="#b9b5b0"/>
        <stop offset=".6" stop-color="#d9d6d2"/>
        <stop offset="1" stop-color="#6f675e"/>
      </linearGradient>
    </defs>
    <rect class="photo photo--top" width="572" height="460" fill="url(#plantTones)" role="img" aria-label="Photo of a QRN Portal table with orange legs installed in a truss plant"/>
    <polygon class="brand-panel" points="250,0 572,0 572,60 470,170 300,170" fill="var(--steel)"/>
    <polyline points="300,170 470,170 572,60" fill="none" stroke="var(--orange)" stroke-width="4"/>
    <polygon class="text-panel" points="0,170 300,170 390,395 0,395" fill="var(--clam)" opacity=".85"/>
    <polygon class="photo-frame" points="0,390 330,390 390,470 390,640 0,640" fill="var(--cream)"/>
    <polygon class="photo photo--bottom" points="0,400 324,400 380,474 380,640 0,640" fill="url(#floorTones)" role="img" aria-label="Photo of the gantry table with orange operator platform on the shop floor"/>
    <rect x="380" y="460" width="192" height="180" fill="#a79a88" role="img" aria-label="Continuation of the installation photo"/>
  </svg>

  <div class="brand"><span class="brand__mark"></span><span>Stratum Machinery</span></div>

  <section class="highlights">
    <h2 class="highlights__title">Our Machine</h2>
    <ul class="highlights__list">
      <li class="highlights__item"><svg class="tick" viewBox="0 0 14 14"><rect x="1" y="1" width="12" height="12" rx="2" fill="none" stroke="var(--orange)" stroke-width="1.6"/><path d="M3.5 7l2.5 2.5L11 4" fill="none" stroke="var(--orange)" stroke-width="1.8"/></svg>Available in 12’ or 14’ wide</li>
      <li class="highlights__item"><svg class="tick" viewBox="0 0 14 14"><rect x="1" y="1" width="12" height="12" rx="2" fill="none" stroke="var(--orange)" stroke-width="1.6"/><path d="M3.5 7l2.5 2.5L11 4" fill="none" stroke="var(--orange)" stroke-width="1.8"/></svg>Side or end eject</li>
      <li class="highlights__item"><svg class="tick" viewBox="0 0 14 14"><rect x="1" y="1" width="12" height="12" rx="2" fill="none" stroke="var(--orange)" stroke-width="1.6"/><path d="M3.5 7l2.5 2.5L11 4" fill="none" stroke="var(--orange)" stroke-width="1.8"/></svg>Heavy duty table top.</li>
      <li class="highlights__item"><svg class="tick" viewBox="0 0 14 14"><rect x="1" y="1" width="12" height="12" rx="2" fill="none" stroke="var(--orange)" stroke-width="1.6"/><path d="M3.5 7l2.5 2.5L11 4" fill="none" stroke="var(--orange)" stroke-width="1.8"/></svg>T-slot opening for jigging</li>
      <li class="highlights__item"><svg class="tick" viewBox="0 0 14 14"><rect x="1" y="1" width="12" height="12" rx="2" fill="none" stroke="var(--orange)" stroke-width="1.6"/><path d="M3.5 7l2.5 2.5L11 4" fill="none" stroke="var(--orange)" stroke-width="1.8"/></svg>All tables built to customers length requirements</li>
    </ul>
  </section>

  <footer class="contact">
    <div class="contact__tab">For Contact Information</div>
    <p class="contact__name">Dario</p>
    <ul class="contact__list">
      <li class="contact__item"><svg class="icon" viewBox="0 0 14 14"><circle cx="7" cy="7" r="6" fill="none" stroke="var(--clam)" stroke-width="1.3"/><path d="M4.8 4h1.4l.6 1.6-.8.6a4 4 0 0 0 1.6 1.6l.6-.8 1.6.6v1.4c-3 .3-5.3-2-5-5z" fill="var(--clam)"/></svg>(800)555-0182</li>
      <li class="contact__item"><svg class="icon" viewBox="0 0 14 14"><circle cx="7" cy="7" r="6" fill="none" stroke="var(--clam)" stroke-width="1.3"/><rect x="3.8" y="5" width="6.4" height="4.4" fill="none" stroke="var(--clam)" stroke-width="1"/><path d="M3.8 5l3.2 2.4L10.2 5" fill="none" stroke="var(--clam)" stroke-width="1"/></svg>dario@lupholdings-example.ca</li>
      <li class="contact__item"><svg class="icon" viewBox="0 0 14 14"><circle cx="7" cy="7" r="6" fill="none" stroke="var(--clam)" stroke-width="1.3"/><circle cx="7" cy="7" r="3.2" fill="none" stroke="var(--clam)" stroke-width="1"/><path d="M3.8 7h6.4M7 3.8v6.4" stroke="var(--clam)" stroke-width="1"/></svg>www.stratummachinery-example.com</li>
    </ul>
  </footer>
</article>
</body>
</html>
```